FLYER für Fortbildung
Zielgruppe
Die Fortbildung, die beworben werden soll, richtet sich an Fachkräfte, die in Kitas arbeiten. In diesem Fall handelt es sich um eine praxisorientierte Online-Live-Fortbildung - dies bedeutet, die TeilnehmerInnen werden während der Online-Fortbildung kontinuierlich durch eine Referentin begleitet. Die Fortbildung erweitert das Wissen und die Kompetenzen der Teilnehmenden.
Aufgabenstellung
Ich freue mich über Vorschläge eines Falzflyers im Format DIN lang. Wie viele Seiten der Flyer umfasst, überlasse ich gerne Ihnen, da dies von Ihrer Gestaltung abhängt.
Falls Sie 1-4 Bilder einfügen möchten, gebe ich Ihnen in den Datei-Upload gerne einige Beispiele, die mir zusagen (zur Auswahl). Darüber hinaus bin ich selbstverständlich auch offen für alternative Vorschläge sowie neue Designs.

```html
<!DOCTYPE html>
<html lang="de">
<head>
<meta charset="utf-8">
<title>Elterngespräche führen – Falzflyer</title>
<link href="https://fonts.googleapis.com/css2?family=Lato:ital,wght@0,300;0,400;0,700;0,900;1,400&display=swap" rel="stylesheet">
<style>
  :root{
    --page:#dedede;
    --light:#c6cddc;
    --slate:#7385a2;
    --slate-dark:#687a98;
    --ink:#333a44;
    --blue-text:#5a6d92;
    --white:#ffffff;
    --photo-warm:#d8cbbd;
    --photo-cool:#a9bccd;
  }
  *{box-sizing:border-box;margin:0;padding:0}
  html,body{width:1200px;height:1177px;overflow:hidden;background:var(--page);font-family:"Lato",sans-serif}
  .sheet{position:absolute;left:195px;width:810px;height:572px;box-shadow:0 4px 14px rgba(0,0,0,.18)}
  .sheet--outside{top:11px}
  .sheet--inside{top:594px}
  .spread{position:absolute;left:0;top:0;width:1190px;height:840px;transform:scale(.6807);transform-origin:0 0;overflow:hidden;background:var(--white)}
  .abs{position:absolute}
  .photo{position:absolute}

  /* outside spread */
  .terms{left:0;top:0;width:388px;height:717px;background:var(--slate);color:var(--white);padding:38px 34px 0 40px;font-size:13.2px;line-height:1.3;text-align:justify;hyphens:auto}
  .terms h3{font-size:15px;font-weight:700;margin-bottom:2px}
  .terms .intro{font-style:italic;margin-bottom:10px}
  .terms h4{font-size:13.5px;font-weight:700;margin-top:8px}
  .privacy{left:40px;top:726px;width:316px;color:var(--blue-text);font-size:10px;line-height:1.35;font-style:italic;text-align:justify}
  .privacy strong{display:block;font-style:normal;font-size:13px;font-weight:700}
  .cover-band{left:388px;top:0;width:802px;height:598px;background:var(--light)}
  .event-meta{left:445px;top:44px;font-size:23px;line-height:1.3;color:var(--ink);font-weight:400}
  .event-meta p{padding-left:12px;position:relative}
  .event-meta p.bar::before{content:"";position:absolute;left:0;top:6px;width:2.5px;height:21px;background:var(--ink)}
  .title{left:790px;top:58px;width:400px;text-align:center;font-size:36px;font-weight:900;letter-spacing:.5px;line-height:1.3;color:var(--ink)}
  .subtitle-tag{background:var(--slate);color:var(--white);font-weight:300;font-size:37px;padding:0 10px;line-height:44px}
  .contact-band{left:388px;top:598px;width:802px;height:119px;background:var(--slate);color:var(--white);padding:22px 0 0 54px;font-size:14.5px;line-height:1.4}
  .contact-band .org{font-size:17px;letter-spacing:.3px;margin-bottom:4px}
  .contact-lines{left:442px;top:726px;color:var(--blue-text);font-size:14.5px;line-height:1.4}
  .brand{display:flex;align-items:center;gap:8px;color:var(--blue-text);font-size:15px;font-weight:400;letter-spacing:.4px}
  .brand-dot{width:14px;height:14px;border-radius:50%;background:var(--slate)}

  /* inside spread */
  .col{top:0;height:840px}
  .col--intro{left:0;width:400px;background:var(--slate)}
  .col--topics{left:400px;width:400px;background:var(--slate)}
  .col--form{left:800px;width:390px;background:var(--light);color:var(--ink)}
  .fold-line{left:400px;top:10px;width:1.5px;height:805px;background:#3e4a5e}
  .intro-text{left:27px;top:383px;width:346px;color:var(--white);font-size:18.5px;line-height:1.16;font-weight:300;text-align:justify;hyphens:auto}
  .intro-text p+p{margin-top:10px}
  .topics-title{left:450px;top:525px;color:#e8ecf3;font-size:23px;font-weight:400}
  .topics{left:416px;top:565px;list-style:none;color:#eef1f6;font-size:15px;line-height:1}
  .topics li{display:flex;align-items:center;gap:12px;height:35.5px}
  .topics svg{width:16px;height:20px;flex:none}
  .form{left:820px;top:36px;width:350px}
  .form h2{text-align:center;font-size:20px;font-weight:400;letter-spacing:.3px;margin-left:14px}
  .form .course{text-align:center;font-size:16px;margin:6px 0 14px}
  .form .note{font-style:italic;font-size:15.5px;line-height:1.18;text-align:justify;padding:0 14px 0 16px}
  .form .date{font-size:14.5px;font-weight:700;margin:14px 0 20px 2px}
  .field{font-size:13.5px;position:relative}
  .rule{height:1px;background:#59616e}
  .consent{font-size:13px;line-height:1.15;text-align:justify}
  .consent strong{display:block;font-size:13.5px}
  .option{display:flex;align-items:center;gap:6px;font-size:13.5px;margin-left:16px}
  .option span.ring{width:7px;height:7px;border:1px solid var(--ink);border-radius:50%}
  .small-italic{font-style:italic;font-size:11.5px}
  .foot{font-size:10px}
</style>
</head>
<body>

<!-- Outside spread -->
<div class="sheet sheet--outside">
  <div class="spread">
    <div class="abs terms">
      <h3>*Teilnahmebedingungen:</h3>
      <p class="intro">Mit Ihrer Anmeldung akzeptieren Sie die folgenden Bedingungen.</p>
      <h4>1. Teilnahmegebühr</h4>
      <p>Die Teilnahmegebühr beträgt 99,00 Euro pro Person, gemäß § 19 UstG (Kleinunternehmerregelung) ohne Umsatzsteuer. Diese ist innerhalb von 30 Tagen nach Erhalt der Rechnung im Voraus zu zahlen. Bei ausbleibender Zahlung behalten wir uns das Recht vor, Ihren Platz an andere Interessierte weiterzugeben.</p>
      <h4>2. Haftungsausschuss</h4>
      <p>Wir schließen jegliche Haftung für Schäden oder Folgeschäden aus, die aus einer Nichterfüllung oder mangelhafter Erfüllung resultieren. Im Falle einer Absage der Veranstaltung durch uns erfolgt eine Rückerstattung der Teilnahmegebühr. Schadensersatzansprüche sind ausgeschlossen. Wir haften nicht für Ergebnisse, die aus der Teilnahme an der Veranstaltung resultieren.</p>
      <h4>3. Widerrufsrecht</h4>
      <p>Kunden, die eine Veranstaltung buchen, haben ein gesetzliches Widerrufsrecht. Der Widerruf muss binnen 14 Tagen nach Vertragsabschluss ohne Angabe von Gründen per E-Mail an anmeldung@gelassen-im-beruf.de erfolgen.</p>
      <h4>4. Rücktritt</h4>
      <p>Ein Rücktritt von der Veranstaltung ist bis vier Wochen vor Beginn der Fortbildung per möglich. Der Rücktritt muss ebenfalls schriftlich per E-Mail erfolgen.</p>
      <h4>5. Geistiges Eigentum</h4>
      <p>Die Inhalte der Veranstaltungen und der dazugehörigen Unterlagen, einschließlich sämtlicher Handouts, Präsentationen und PDFs, sind geistiges Eigentum von uns. Die Vervielfältigung oder Weitergabe ist ohne unsere ausdrückliche Genehmigung nicht gestattet.</p>
    </div>
    <div class="abs privacy">
      <strong>Datenschutz:</strong>
      Ihre personenbezogenen Daten (Name, E-Mail-Adresse, Datum und Titel der besuchten Veranstaltung) werden ausschließlich zur Abwicklung und zur Ausstellung einer Teilnahmebescheinigung verwendet. Eine Weitergabe an Dritte erfolgt nicht. Sie haben das Recht auf Auskunft, Berichtigung und Löschung Ihrer Daten.
    </div>

    <div class="abs cover-band"></div>
    <div class="abs event-meta">
      <p class="bar">Live-Online-Fortbildung für</p>
      <p>Mitarbeitende in Kitas</p>
      <p class="bar">Montag, den 30. März 2026</p>
      <p class="bar">09:00 bis 15:00 Uhr</p>
    </div>
    <div class="abs title">ELTERNGESPRÄCHE<br>FÜHREN</div>
    <div class="photo" style="left:388px;top:198px;width:401px;height:349px;background:linear-gradient(135deg,#b9cde0 0%,#9fb6c9 45%,#8e8f8c 75%,#cfc3b0 100%)" role="img" aria-label="Foto: Pädagogische Fachkraft mit Brille im Gespräch am Tisch"></div>
    <div class="photo" style="left:789px;top:211px;width:401px;height:336px;background:linear-gradient(160deg,#e7e1d9 0%,#cdbfb0 45%,#a8a8b0 80%,#d5d2cc 100%)" role="img" aria-label="Foto: Elternpaar mit Tochter auf dem Sofa"></div>
    <div class="abs subtitle-tag" style="left:968px;top:168px">Grundlagen</div>

    <div class="abs contact-band">
      <p class="org">GELASSEN IM BERUF</p>
      <p>Marlene Vogt</p>
      <p>Lindenweg 45</p>
      <p>67433 Neustadt</p>
    </div>
    <div class="abs contact-lines">
      <p>Telefon: +49 160 48203917</p>
      <p>E-Mail: kontakt@vogt-beispiel.de</p>
      <p>Homepage: www.vogt-beispiel.de</p>
    </div>
    <div class="abs brand" style="left:912px;top:770px"><span class="brand-dot"></span>GELASSEN IM BERUF</div>
  </div>
</div>

<!-- Inside spread -->
<div class="sheet sheet--inside">
  <div class="spread">
    <div class="abs col col--intro"></div>
    <div class="abs col col--topics"></div>
    <div class="abs col col--form"></div>
    <div class="abs fold-line"></div>

    <div class="photo" style="left:49px;top:40px;width:300px;height:300px;border-radius:50%;background:radial-gradient(circle at 40% 40%,#e9e6dc 0%,#9fae8a 55%,#4d5a48 100%)" role="img" aria-label="Foto: Erzieherin im Gespräch mit einer Mutter"></div>
    <div class="abs intro-text">
      <p>Diese Fortbildung richtet sich an Berufsanfänger, unsichere Fachkräfte und alle, die ihre Kenntnisse bezüglich Elterngesprächen auffrischen möchten. Ziel ist es, Ihnen Sicherheit und Selbstvertrauen im Umgang mit Eltern zu geben.</p>
      <p>Benötigt wird ein PC oder Laptop mit Webcam/Mikrofon.</p>
    </div>
    <div class="photo" style="left:27px;top:600px;width:346px;height:240px;background:linear-gradient(120deg,#3f5f9a 0%,#b78a6c 45%,#e2d2c4 70%,#6d4f3c 100%)" role="img" aria-label="Foto: Erzieherin übergibt ein Kleinkind an die Mutter"></div>

    <div class="photo" style="left:426px;top:40px;width:347px;height:432px;background:linear-gradient(150deg,#f2ece4 0%,#e4d7c9 45%,#c8b6a4 80%,#9aa6b8 100%)" role="img" aria-label="Foto: Lächelnde Frau reicht die Hand zur Begrüßung"></div>
    <div class="abs topics-title">Inhalte der Fortbildung:</div>
    <ul class="abs topics">
      <li><svg viewBox="0 0 16 20"><path d="M1 11 L5 18 L15 1" fill="none" stroke="#eef1f6" stroke-width="2"/></svg>Theoretische Modelle der Gesprächsführung</li>
      <li><svg viewBox="0 0 16 20"><path d="M1 11 L5 18 L15 1" fill="none" stroke="#eef1f6" stroke-width="2"/></svg>Effektive Vorbereitung auf Elterngespräche</li>
      <li><svg viewBox="0 0 16 20"><path d="M1 11 L5 18 L15 1" fill="none" stroke="#eef1f6" stroke-width="2"/></svg>Gesprächseinstieg</li>
      <li><svg viewBox="0 0 16 20"><path d="M1 11 L5 18 L15 1" fill="none" stroke="#eef1f6" stroke-width="2"/></svg>Umgang mit schwierigen Gesprächssituationen</li>
      <li><svg viewBox="0 0 16 20"><path d="M1 11 L5 18 L15 1" fill="none" stroke="#eef1f6" stroke-width="2"/></svg>Deeskalation / Konfliktlösungsstrategien</li>
      <li><svg viewBox="0 0 16 20"><path d="M1 11 L5 18 L15 1" fill="none" stroke="#eef1f6" stroke-width="2"/></svg>Möglichkeiten zum Üben und Austausch</li>
    </ul>

    <div class="abs form">
      <h2>ANMELDUNG ZUR FORTBILDUNG</h2>
      <p class="course">Elterngespräche führen – Grundlagen</p>
      <p class="note">Bitte füllen Sie das Formular aus und senden Sie es an anmeldung@gelassen-im-beruf.de. Mit Ihrer Anmeldung akzeptieren Sie die aufgeführten Teilnahmebedingungen*</p>
      <p class="date">Am 30. März 2026 von 09:00 – 15:00 Uhr (online)</p>
      <p class="field" style="margin-bottom:20px">Vor- und Zuname:</p>
      <div class="rule" style="margin-bottom:12px"></div>
      <p class="field" style="margin-bottom:26px">Rechnungsadresse:</p>
      <div class="rule" style="margin-bottom:42px"></div>
      <div class="rule" style="margin-bottom:42px"></div>
      <div class="rule" style="margin-bottom:16px"></div>
      <p class="field" style="margin-bottom:22px">Ihre E-Mail-Adresse für den Zugangslink:</p>
      <div class="rule" style="margin-bottom:22px"></div>
      <p class="consent"><strong>Marketing-Zustimmung</strong>Ich möchte über zukünftige Fortbildungsangebote für Mitarbeitende in Kitas informiert werden. Sie können der Verwendung Ihrer Daten jederzeit kostenlos widersprechen.</p>
      <p class="field" style="margin:12px 0 14px">Bitte wählen Sie:</p>
      <p class="option" style="margin-bottom:13px"><span class="ring"></span>Ja, ich möchte informiert werden.</p>
      <p class="option" style="margin-bottom:22px"><span class="ring"></span>Nein, ich möchte keine Informationen erhalten.</p>
      <p class="small-italic" style="margin-bottom:26px">Ich habe die Teilnahmebedingungen gelesen und akzeptiere diese.</p>
      <div class="rule" style="margin-bottom:6px"></div>
      <p class="field" style="display:flex;gap:82px;margin-bottom:12px"><span>Ort, Datum</span><span>Unterschrift</span></p>
      <p class="foot">*(gemäß § 19 UstG Kleinunternehmerregelung, daher ohne Umsatzsteuer)</p>
    </div>
  </div>
</div>

</body>
</html>
```